BUSINESS CARD DESIGN

NAME- TODD MASVERIK
PHONE NUMER - 808- 451-7082
EMAIL- OFFICE@VORLINDE-GRADEWAY.COM
BACK OF CARD- SPEACIALIZES IN LAND CLEARING, FORESTRY MUCLHING AND EXCAVATION

Contact Information for Business Card

NAME- TODD MASVERIK PHONE NUMER - 808- 451-7082 EMAIL- OFFICE@VORLINDE-GRADEWAY.COM BACK OF CARD- SPEACIALIZES IN LAND CLEARING , MUCLHING AND EXCAVATION

```html
<!DOCTYPE html>
<html lang="en">
<head>
<meta charset="utf-8">
<title>Vorlinde Gradeway – Business Card</title>
<link href="https://fonts.googleapis.com/css2?family=Montserrat:wght@400;500;700&display=swap" rel="stylesheet">
<style>
  :root {
    --stage: #2a2a2a;
    --card: #161616;
    --gold: #f5b21b;
    --silver: #a9a9a9;
    --white: #f2f2f2;
  }
  * { box-sizing: border-box; margin: 0; padding: 0; }
  html, body { width: 1200px; height: 875px; overflow: hidden; }
  body {
    background: var(--stage);
    font-family: "Montserrat", Arial, sans-serif;
    display: flex; align-items: center; justify-content: center; gap: 40px;
  }
  .card {
    width: 560px; height: 320px; background: var(--card);
    border-radius: 18px; position: relative; overflow: hidden;
  }
  /* Back side */
  .card-back { display: flex; align-items: center; justify-content: center; gap: 16px; }
  .card-back .brand-dot { width: 46px; height: 46px; border-radius: 50%; background: var(--silver); }
  .card-back .brand-name { color: var(--silver); font-weight: 700; font-size: 26px; letter-spacing: 1px; }
  /* Front side */
  .card-front .brand {
    position: absolute; left: 36px; top: 74px; width: 190px;
    display: flex; flex-direction: column; align-items: center; gap: 12px; text-align: center;
  }
  .card-front .brand-dot { width: 54px; height: 54px; border-radius: 50%; background: var(--gold); }
  .card-front .brand-name { color: var(--gold); font-weight: 700; font-size: 18px; letter-spacing: 1px; line-height: 1.25; }
  .divider { position: absolute; left: 246px; top: 50px; width: 2px; height: 150px; background: var(--gold); }
  .contact { position: absolute; left: 270px; top: 48px; }
  .person-name { color: var(--gold); font-weight: 700; font-size: 24px; letter-spacing: .5px; }
  .person-title { color: var(--white); font-size: 13px; margin: 4px 0 16px; }
  .contact-list { list-style: none; }
  .contact-list li { color: var(--white); font-size: 12.5px; display: flex; align-items: center; gap: 8px; margin-bottom: 7px; }
  .contact-list svg { width: 12px; height: 12px; fill: var(--gold); flex: none; }
  .tagline {
    position: absolute; left: 0; right: 0; bottom: 34px; text-align: center;
    color: var(--white); font-size: 13px; font-weight: 500; letter-spacing: .3px;
  }
</style>
</head>
<body>
  <section class="card card-back">
    <span class="brand-dot"></span>
    <span class="brand-name">VORLINDE GRADEWAY LLC</span>
  </section>

  <section class="card card-front">
    <div class="brand">
      <span class="brand-dot"></span>
      <span class="brand-name">VORLINDE GRADEWAY LLC</span>
    </div>
    <div class="divider"></div>
    <div class="contact">
      <h1 class="person-name">TODD MASVERIK</h1>
      <p class="person-title">Managing Director</p>
      <ul class="contact-list">
        <li><svg viewBox="0 0 24 24"><path d="M6.6 10.8a15.1 15.1 0 0 0 6.6 6.6l2.2-2.2a1 1 0 0 1 1-.25 11.4 11.4 0 0 0 3.6.57 1 1 0 0 1 1 1V20a1 1 0 0 1-1 1A17 17 0 0 1 3 4a1 1 0 0 1 1-1h3.5a1 1 0 0 1 1 1c0 1.25.2 2.45.57 3.57a1 1 0 0 1-.25 1z"/></svg>808- 451-7082</li>
        <li><svg viewBox="0 0 24 24"><path d="M2 5h20v14H2z M2 5l10 8 10-8" /></svg>office@vorlinde-gradeway.com</li>
        <li><svg viewBox="0 0 24 24"><circle cx="12" cy="12" r="10"/></svg>www.vorlinde-gradeway.com</li>
      </ul>
    </div>
    <p class="tagline">SPEACIALIZES IN LAND CLEARING , MUCLHING AND EXCAVATION</p>
  </section>
</body>
</html>
```